Halvorn - Refresh the look and feel of an existing website

We currently have an existing website www.halvornworldadvisory.example however it needs a more refreshed 'look and feel'. We are a professional consultancy that works with large corporate organisations and government. Our 'tag line' is A New Way of Thinking. We want the site to communicate "Innovation" and Leading Edge Thinking.

Target Market(s)

Corporate and Professional Clients - Organisation and Business Change

Industry/Entity Type

Management Consulting

Number of Pages Required

1 page

Font styles to use
Sans Serif

Requirements
Must have
• Must have a professional Corporate look and feel. Header 'imagery' is ok but boxes on front page need changing ... along with the words. The focus on home page needs to 'call out' 3 main consulting areas:-
• - Change & Transformation Specialists
• - Innovative Solutions
• - Digital Transformation
• Tag Line for business is ... A New Way of Thinking (Highlighting Halvorn as 'Thought Leaders' in business)
Nice to have
• Less "words' more imagery. Possibly an area for a 'video' or recent articles/blogs on the front page. Needs to have more of an 'interactive' feel. We are open to suggestions.
Should not have
• NA

```html
<!DOCTYPE html>
<html lang="en">
<head>
<meta charset="utf-8">
<title>Halvorn – A New Way of Thinking</title>
<link rel="stylesheet" href="https://fonts.googleapis.com/css2?family=Raleway:wght@400;500;600;700&family=Questrial&display=swap">
<style>
:root{
  --navy:#2a4263;
  --navy-band:#253d5c;
  --navy-deep:#223654;
  --footer:#2c4262;
  --footer-bar:#233757;
  --orange:#f15a29;
  --ink:#1f3350;
  --text:#3c4a5c;
  --muted:#6b7687;
  --light:#f2f2f2;
  --btn:#eeeeee;
  --white:#ffffff;
  --line:#e6e9ee;
}
*{margin:0;padding:0;box-sizing:border-box}
html,body{width:1200px;height:2635px;overflow:hidden;background:var(--white)}
body{font-family:"Questrial",sans-serif;color:var(--text);position:relative}
h1,h2,h3,h4,.nav,.btn,.brand{font-family:"Raleway",sans-serif}
section,header,footer{position:relative;width:1200px;overflow:hidden}
.abs{position:absolute}
.btn{position:absolute;display:flex;align-items:center;justify-content:center;width:158px;height:34px;background:var(--btn);color:var(--navy);font-size:13px;font-weight:600;border:1px solid #dcdcdc}
.btn--solid{background:var(--navy);color:var(--white);border-color:var(--navy)}

/* hero */
.hero{height:548px}
.hero__photo{position:absolute;inset:0;background:linear-gradient(100deg,#3a4d66 0%,#5b6d84 30%,#6f7f93 55%,#4f627b 80%,#3c4f68 100%)}
.hero__shade{position:absolute;inset:0;background:rgba(34,54,84,.45)}
.brand{position:absolute;left:84px;top:26px;display:flex;align-items:center;gap:10px;color:var(--white);font-size:22px;font-weight:600;letter-spacing:1px}
.brand__dot{width:30px;height:30px;border:2px solid var(--white);border-radius:50%}
.nav{position:absolute;top:29px;left:0;width:100%;font-size:13px;color:var(--white)}
.nav span{position:absolute;white-space:nowrap}
.search{position:absolute;left:1090px;top:26px}
.hero h1{position:absolute;top:210px;width:100%;text-align:center;color:var(--white);font-size:46px;font-weight:600}
.hero p{position:absolute;top:292px;left:205px;width:790px;text-align:center;color:var(--white);font-size:16px;line-height:26px}
.hero .btn{left:520px;top:398px}

/* services */
.services{height:541px}
.section-title{position:absolute;width:100%;text-align:center;color:var(--ink);font-size:22px;font-weight:600}
.section-sub{position:absolute;width:100%;text-align:center;color:var(--text);font-size:15px}
.services .section-title{top:46px}
.services .section-sub{top:92px}
.services__link{position:absolute;left:258px;top:232px;width:684px;height:1px;background:var(--line)}
.service{position:absolute;top:167px;width:300px;text-align:center}
.service__ring{width:130px;height:130px;margin:0 auto;border-radius:50%;border:1px solid #f0f1f4;background:var(--white);display:flex;align-items:center;justify-content:center}
.service__core{width:106px;height:106px;border-radius:50%;border:1px solid var(--line);display:flex;align-items:center;justify-content:center;background:var(--white)}
.service--active .service__core{background:var(--navy);border-color:var(--navy)}
.service h3{margin-top:26px;color:var(--ink);font-size:16px;font-weight:700}
.service p{width:255px;margin:10px auto 0;font-size:14px;line-height:18px}
.service .btn{left:71px;top:270px}

/* video band */
.video{height:348px;background:var(--navy-band);color:var(--white)}
.video h3{position:absolute;left:86px;top:96px;font-size:17px;font-weight:700}
.video p{position:absolute;left:86px;top:124px;width:380px;font-size:14px;line-height:18px}
.video .btn{left:86px;top:214px}
.video__media{position:absolute;left:527px;top:0;width:583px;height:348px;background:linear-gradient(90deg,#2c4463 0%,#3d4f66 20%,#1d2430 40%,#e9ecef 50%,#dfe3e8 65%,#1d2430 82%,#3d4f66 95%,#2c4463 100%)}

/* blog */
.blog{height:492px}
.blog .section-title{top:52px}
.blog .section-sub{top:98px}
.blog__frame{position:absolute;left:84px;top:144px;width:215px;height:295px;border:3px solid var(--orange)}
.blog__photo{position:absolute;left:100px;top:160px;width:487px;height:262px;background:linear-gradient(135deg,#cfd9e4 0%,#b9c8d8 40%,#8ea3b9 70%,#5e6f82 100%)}
.post{position:absolute;left:622px;width:480px;padding-left:16px;border-left:3px solid var(--orange)}
.post__meta{font-size:10px;color:var(--muted)}
.post__meta em{font-style:normal;color:var(--orange)}
.post h4{margin-top:6px;color:var(--ink);font-size:14px;font-weight:700}
.post p{position:relative;left:-19px;margin-top:10px;width:480px;font-size:14px;line-height:18px}
.post .more{position:relative;left:-19px;display:block;margin-top:8px;font-family:"Raleway",sans-serif;font-size:10px;font-weight:700;color:var(--ink)}

/* recent articles */
.recent{height:416px;background:var(--light)}
.recent h2{position:absolute;left:93px;top:30px;color:var(--ink);font-size:22px;font-weight:600}
.article__box{position:absolute;top:109px;width:253px;height:185px;background:var(--navy);color:var(--white);padding:26px 20px}
.article__box h4{font-size:14px;font-weight:700}
.article__box p{margin-top:14px;font-size:14px;line-height:18px}
.article__box .read{display:block;margin-top:12px;font-size:14px}
.article__photo{position:absolute;top:74px;width:230px;height:244px;background:linear-gradient(135deg,#e8ebef 0%,#c7ccd3 45%,#8d96a3 100%)}
.article__date{position:absolute;top:74px;width:60px;height:60px;background:var(--orange);color:var(--white);font-family:"Raleway",sans-serif;font-size:11px;font-weight:600;text-align:center;line-height:14px;padding-top:16px}
.dots{position:absolute;left:575px;top:358px;display:flex;gap:6px}
.dots i{width:12px;height:12px;border-radius:50%;background:var(--navy)}
.dots i.on{background:var(--orange)}

/* footer */
.footer{height:238px;background:var(--footer);color:var(--white)}
.fcol{position:absolute;top:30px;width:230px}
.fcol h4{font-size:13px;font-weight:700;letter-spacing:.5px;padding-bottom:10px;width:185px;border-bottom:1px solid rgba(255,255,255,.35)}
.fcol p{margin-top:18px;font-size:13px;line-height:23px;width:225px}
.fcol ul{list-style:none;margin-top:16px;font-size:13px;line-height:23.4px}
.fcol li{position:relative;padding-left:22px}
.fcol li::before{content:"";position:absolute;left:2px;top:8px;border-top:7px solid var(--white);border-left:7px solid transparent}
.contact{display:flex;gap:18px;font-size:13px;line-height:18px;margin-top:16px}
.contact svg{flex:none;margin-top:2px}
.bar{height:52px;background:var(--footer-bar);color:var(--white);font-size:13px}
.bar span{position:absolute;top:17px}
</style>
</head>
<body>

<header class="hero">
  <div class="hero__photo" role="img" aria-label="Photo of two colleagues smiling in a bright office"></div>
  <div class="hero__shade"></div>
  <div class="brand"><span class="brand__dot"></span>HALVORN</div>
  <nav class="nav">
    <span style="left:418px">Home</span>
    <span style="left:489px">About Us</span>
    <span style="left:578px">Our Services</span>
    <span style="left:687px">Solutions</span>
    <span style="left:775px">What's Happening</span>
    <span style="left:922px">Contact Us</span>
  </nav>
  <svg class="search" width="22" height="22" viewBox="0 0 22 22" fill="none" stroke="#fff" stroke-width="2.4"><circle cx="9" cy="9" r="6.5"/><path d="M14 14l6 6"/></svg>
  <h1>A New Way of Thinking</h1>
  <p>Lorem ipsum dolor sit amet, consectetuer adipiscing elit, sed diam nonummy nibh euismod tincidunt ut laoreet dolore magna aliquam erat volutpat. Ut wisi praesent luptatum zzril delenit augue duis dolore te feugait nulla facilisi.</p>
  <span class="btn">Learn More</span>
</header>

<section class="services">
  <h2 class="section-title">What We Have?</h2>
  <p class="section-sub">Duis mattis semper risus sit amet porttitor turpis egestas vitae</p>
  <div class="services__link"></div>

  <div class="service" style="left:108px">
    <div class="service__ring"><div class="service__core">
      <svg width="48" height="48" viewBox="0 0 48 48" fill="none" stroke="#5d8fc7" stroke-width="2.5"><path d="M24 6a18 18 0 0 1 17 12"/><path d="M42 30a18 18 0 0 1-16 12"/><path d="M14 40A18 18 0 0 1 6 22"/><circle cx="24" cy="24" r="7" fill="#5d8fc7"/><circle cx="24" cy="24" r="11" stroke-dasharray="4 3"/></svg>
    </div></div>
    <h3>Transformation Specialists</h3>
    <p>Lorem ipsum dolor sit amet, nonummy nibh euismod tincidunt ut laoreet dolore magna aliquam erat volutpat.</p>
    <span class="btn">Learn More</span>
  </div>

  <div class="service service--active" style="left:449px">
    <div class="service__ring"><div class="service__core">
      <svg width="52" height="52" viewBox="0 0 52 52" fill="none" stroke="#fff" stroke-width="2"><circle cx="26" cy="16" r="8"/><path d="M23 24h6M24 27h4"/><path d="M26 3v3M14 8l2 2M38 8l-2 2M10 16h3M39 16h3"/><path d="M10 48c0-10 7-16 16-16s16 6 16 16z" fill="#fff"/><path d="M26 34l-3 8 3 4 3-4z" fill="#2a4263" stroke="none"/></svg>
    </div></div>
    <h3>Innovative Solutions</h3>
    <p>Lorem ipsum dolor sit amet, nonummy nibh euismod tincidunt ut laoreet dolore magna aliquam erat volutpat.</p>
    <span class="btn btn--solid">Learn More</span>
  </div>

  <div class="service" style="left:792px">
    <div class="service__ring"><div class="service__core">
      <svg width="56" height="44" viewBox="0 0 56 44" fill="none" stroke="#2a4263" stroke-width="2.2"><rect x="3" y="4" width="22" height="16"/><rect x="24" y="14" width="28" height="20"/><path d="M38 34v5M32 40h12M14 20v6h10"/><path d="M28 24l4-3 4 2 5-5"/></svg>
    </div></div>
    <h3>Digital Transformation</h3>
    <p>Lorem ipsum dolor sit amet, nonummy nibh euismod tincidunt ut laoreet dolore magna aliquam erat volutpat.</p>
    <span class="btn">Learn More</span>
  </div>
</section>

<section class="video">
  <h3>Lorem ipsum dolor sit amet,</h3>
  <p>Lorem ipsum dolor sit amet, nonummy nibh euismod tincidunt ut laoreet dolore magna aliquam erat volutpat.Duis autem vel eum iriure dolor in hendrerit in vulputate velit esse molestie consequat,</p>
  <span class="btn">Watch More</span>
  <div class="video__media" role="img" aria-label="Photo of hands holding a tablet playing the company introduction video"></div>
</section>

<section class="blog">
  <h2 class="section-title">Blog News</h2>
  <p class="section-sub">Duis mattis semper risus sit amet porttitor turpis egestas vitae</p>
  <div class="blog__frame"></div>
  <div class="blog__photo" role="img" aria-label="Photo of a business team meeting around a table with a chart on a screen"></div>

  <article class="post" style="top:166px">
    <div class="post__meta">May 25,2016 &nbsp;| Posted by <em>Admin</em></div>
    <h4>Lorem ipsum dolor sit amet, lorem Ipsum</h4>
    <p>Lorem ipsum dolor sit amet, consectetuer adipiscing elit, sed diam erat volutpat. Ut wisi enim ad minim veniam,</p>
    <span class="more">READ MORE</span>
  </article>
  <article class="post" style="top:313px">
    <div class="post__meta">May 25,2016 &nbsp;| Posted by <em>Admin</em></div>
    <h4>Lorem ipsum dolor sit amet, lorem Ipsum</h4>
    <p>Lorem ipsum dolor sit amet, consectetuer adipiscing elit, sed diam erat volutpat. Ut wisi enim ad minim veniam,</p>
    <span class="more">READ MORE</span>
  </article>
</section>

<section class="recent">
  <h2>Recent Articles</h2>

  <div class="article__box" style="left:88px">
    <h4>Lorem Ipsum Dummy</h4>
    <p>Lorem ipsum dolor sit amet, consectetuer adipiscing elit, sed mod tincidunt ut laoreet dolore magna aliquam erat volutpat.</p>
    <span class="read">Read More &rarr;</span>
  </div>
  <div class="article__photo" style="left:341px" role="img" aria-label="Photo of colleagues working together at a whiteboard"></div>
  <div class="article__date" style="left:341px">29<br>NOV</div>

  <div class="article__box" style="left:625px">
    <h4>Lorem Ipsum Dummy</h4>
    <p>Lorem ipsum dolor sit amet, consectetuer adipiscing elit, sed mod tincidunt ut laoreet dolore magna aliquam erat volutpat.</p>
    <span class="read">Read More &rarr;</span>
  </div>
  <div class="article__photo" style="left:878px;background:linear-gradient(135deg,#dfe4ea 0%,#aeb9c6 50%,#5d6c7f 100%)" role="img" aria-label="Photo of a business handshake"></div>
  <div class="article__date" style="left:878px">29<br>NOV</div>

  <div class="dots"><i></i><i class="on"></i><i></i></div>
</section>

<footer>
  <div class="footer">
    <div class="fcol" style="left:91px">
      <h4>ABOUT US</h4>
      <p>Lorem Ipsum is simply dummy text of the printing and typesetting industry. Lorem Ipsum has been the industry's standard dummy text ever since the a type specimen book.</p>
    </div>
    <div class="fcol" style="left:353px">
      <h4>INFORMATION</h4>
      <ul><li>List Orders</li><li>Legal Notice</li><li>About us</li><li>Contact us</li><li>Front page</li><li>My Account</li></ul>
    </div>
    <div class="fcol" style="left:610px">
      <h4>CATEGORY</h4>
      <ul><li>Active Wear</li><li>Lorem Ipsum</li><li>Lorem Ipsum</li><li>Lorem Ipsum</li><li>Lorem Ipsum</li><li>Lorem Ipsum</li></ul>
    </div>
    <div class="fcol" style="left:873px;width:260px">
      <h4>CONTACT US</h4>
      <div class="contact"><svg width="16" height="14" viewBox="0 0 16 14" fill="#fff"><path d="M8 0l8 7h-2v7h-4V9H6v5H2V7H0z"/></svg><span>48 Larchmont Avenue, New York USA 10012</span></div>
      <div class="contact"><svg width="16" height="16" viewBox="0 0 16 16" fill="#fff"><path d="M3 1l3 3-2 2c1 2 3 4 5 5l2-2 3 3-2 3C7 15 1 9 1 3z"/></svg><span>+1-555-0147</span></div>
      <div class="contact"><svg width="16" height="12" viewBox="0 0 16 12" fill="none" stroke="#fff" stroke-width="1.4"><rect x="1" y="1" width="14" height="10"/><path d="M1 1l7 6 7-6"/></svg><span>hello@halvorn.example</span></div>
    </div>
  </div>
  <div class="bar" style="position:relative">
    <span style="left:95px">Management Consulting . All Rights Reserved.</span>
    <span style="left:921px">FAQ's</span>
    <span style="left:977px">Sitemap</span>
    <span style="left:1049px">Contact</span>
  </div>
</footer>

</body>
</html>
```